We need a business card design for a new brand within our existing financial marketing business. Our new brand is www.qalvenport.co.uk

We attach various logo files - please use the version that will produce the sharpest image on the business card.

We are flexible about shape of card etc. Please think outside the box as to what goes on front and what goes on back of the card.

The card needs to be corporate, but really catch the eye ( e.g. premium translucent cards on plastic etc or metal cards or shiny surface etc )

We want to be able to amend the card (once the design has been agreed ) to add additional staff details, but the text to go on it will be generic

Details to go on card ( for the first generic one) are fairly minimal as we don't like cluttered business cards:-

Owen Tagget
Managing Director

Mobile: 07852 418 207
Email: o.tagget@qalvenport.co.uk

Financial

```html
<!DOCTYPE html>
<html lang="en">
<head>
<meta charset="utf-8">
<title>Qalvenport Business Card</title>
<link rel="stylesheet" href="https://fonts.googleapis.com/css2?family=Exo+2:wght@400;500;600&display=swap">
<style>
  :root {
    --blue: #1f75bd;
    --gold: #e2b324;
    --white: #ffffff;
    --ink: #2b2b2b;
    --stage: #e9ebee;
    --card-w: 400px;
    --card-h: 700px;
  }
  * { margin: 0; padding: 0; box-sizing: border-box; }
  html, body { width: 1200px; height: 974px; overflow: hidden; }
  body {
    background: var(--stage);
    font-family: "Exo 2", sans-serif;
    display: flex;
    align-items: center;
    justify-content: center;
    gap: 100px;
  }
  .card {
    position: relative;
    width: var(--card-w);
    height: var(--card-h);
    background: var(--blue);
    box-shadow: 0 10px 30px rgba(0,0,0,0.15);
    overflow: hidden;
  }
  .card-body {
    position: absolute;
    inset: 0 0 88px 0;
    background: var(--white);
    border-bottom-left-radius: 30px;
    border-bottom-right-radius: 30px;
  }
  .card-footer {
    position: absolute;
    left: 0; right: 0; bottom: 0;
    height: 88px;
    display: flex;
    align-items: center;
    justify-content: center;
    color: var(--white);
    font-size: 19px;
    font-weight: 500;
    letter-spacing: 1px;
  }
  .brand {
    display: flex;
    align-items: center;
    justify-content: center;
    gap: 10px;
    color: var(--blue);
    font-weight: 500;
    font-size: 42px;
    letter-spacing: 0.5px;
  }
  .brand-mark {
    width: 26px; height: 26px;
    background: var(--gold);
  }
  .back .brand { margin-top: 200px; }
  .front .brand { height: 130px; padding-top: 20px; }
  .band-name {
    background: var(--blue);
    height: 86px;
    display: flex;
    flex-direction: column;
    justify-content: center;
    padding-left: 120px;
    color: var(--gold);
    text-transform: uppercase;
  }
  .person-name { font-size: 26px; font-weight: 600; letter-spacing: 1px; line-height: 1.1; }
  .person-role { font-size: 18px; font-weight: 500; letter-spacing: 1.5px; }
  .contact-row {
    display: flex;
    align-items: center;
    gap: 26px;
    padding-left: 60px;
    color: var(--ink);
    font-size: 19px;
    letter-spacing: 1px;
    line-height: 1.45;
  }
  .row-phone { height: 120px; }
  .row-email { height: 96px; background: var(--gold); }
  .row-address { height: 130px; }
  .icon { width: 34px; height: 34px; flex: none; fill: var(--ink); }
</style>
</head>
<body>

  <div class="card back">
    <div class="card-body">
      <div class="brand"><span class="brand-mark"></span><span>Qalvenport</span></div>
    </div>
    <div class="card-footer">www.qalvenport.co.uk</div>
  </div>

  <div class="card front">
    <div class="card-body">
      <div class="brand"><span class="brand-mark"></span><span>Qalvenport</span></div>
      <div class="band-name">
        <span class="person-name">Owen Tagget</span>
        <span class="person-role">Managing Director</span>
      </div>
      <div class="contact-row row-phone">
        <svg class="icon" viewBox="0 0 34 34" aria-hidden="true">
          <path d="M3 10c0-3 4-5 14-5s14 2 14 5v3h-7v-3c-2-1-12-1-14 0v3H3z"/>
          <path d="M9 14h16l4 14H5z M13 18a4 4 0 1 0 8 0a4 4 0 1 0-8 0z" fill-rule="evenodd"/>
        </svg>
        <div>07852 418 207</div>
      </div>
      <div class="contact-row row-email">
        <svg class="icon" viewBox="0 0 34 34" aria-hidden="true">
          <path d="M3 8h28v18H3z M5 10l12 9l12-9z" fill-rule="evenodd"/>
        </svg>
        <div>o.tagget@qalvenport.co.uk</div>
      </div>
      <div class="contact-row row-address">
        <svg class="icon" viewBox="0 0 34 34" aria-hidden="true">
          <path d="M17 2a10 10 0 0 0-10 10c0 8 10 20 10 20s10-12 10-20A10 10 0 0 0 17 2z M17 8a4 4 0 1 1 0 8a4 4 0 1 1 0-8z" fill-rule="evenodd"/>
        </svg>
        <div>14 Harbour Lane,<br>2nd Floor Suite W.</div>
      </div>
    </div>
    <div class="card-footer">www.qalvenport.co.uk</div>
  </div>

</body>
</html>
```